Flyer Design Project

We need a flyer design for a 1 year old domestic cleaning company based in Wiltshire, England. We provide households with high quality, hard working cleaners. We would like to see designs which use blue (the colour on the logo attatched). The final design should communicate a clean, premier and thorough service in a clear and bold way. We would like the flyer to be A5 with a single sided design. We have attached an A5 word document with the words we would like to be used in the design, what we need is for you to give it some life, colour, artwork and a professional touch. We are perfectionsists which we would like to illustrate to our customer through this flyer.
Updates

payment has been guaranteed!

Sorry..... please no pictures of females on the designs. many thanks

Target Market(s)

females with higher than average income, aged 30-50. Have families and work 9-5.

Industry/Entity Type

It Company

Requirements
Must have
• The flyer must include the logo attatched and the words in the A5 document attatched. With RELIABLE CLEANERS preferably the headline. A5 - single sided.
The Flyer must also include our introductory offer.....
First Clean FREE
Allow us to demonstrate our standards

this should be emphasised.

PLEASE NOTE: can this be added to the list of words on the flyer please:

Ironing service - one day turn around
Nice to have
• some pictures - nothing cheesey. Again, pictures should communicate our modern professional approach.

```html
<!DOCTYPE html>
<html lang="en">
<head>
<meta charset="utf-8">
<title>Brookfield Cleaners – Flyer</title>
<link rel="stylesheet" href="https://fonts.googleapis.com/css2?family=Marcellus&family=Arimo:wght@400;700&display=swap">
<style>
  :root {
    --stage: #0d1a2e;
    --ink: #1a1a1a;
    --brand-blue: #1f5fae;
    --offer-red: #d8232a;
    --band-grey: #b8b8ba;
    --card-white: #fbfbfb;
    --wall-light: #e9e9e7;
    --wall-mid: #c9c9c6;
    --floor: #f2f2f0;
  }
  * { box-sizing: border-box; margin: 0; padding: 0; }
  html, body { width: 1200px; height: 817px; overflow: hidden; }
  body { background: var(--stage); position: relative; }

  .flyer {
    position: absolute; left: 348px; top: 51px;
    width: 505px; height: 715px;
    background: var(--floor);
    overflow: hidden;
    font-family: "Arimo", Arial, sans-serif;
    color: var(--ink);
  }
  .hero-photo {
    position: absolute; left: 0; top: 0; width: 505px; height: 585px;
    background:
      linear-gradient(180deg, rgba(255,255,255,0) 78%, var(--floor) 80%),
      radial-gradient(ellipse at 70% 35%, var(--wall-light) 0%, var(--wall-mid) 75%);
  }

  .brand {
    position: absolute; left: 98px; top: 92px;
    display: flex; align-items: center; gap: 12px;
  }
  .brand-mark { width: 34px; height: 34px; background: var(--brand-blue); }
  .brand-name {
    font-family: "Marcellus", Georgia, serif;
    font-size: 34px; color: var(--ink); letter-spacing: 0.5px;
  }
  .tagline {
    position: absolute; left: 175px; top: 155px;
    font-family: "Marcellus", Georgia, serif;
    font-size: 19px; font-weight: 700;
  }

  .benefits {
    position: absolute; left: 72px; top: 198px;
    list-style: none; font-size: 16px; line-height: 17.5px;
  }

  .offer-badge {
    position: absolute; left: 220px; top: 305px;
    width: 290px; height: 130px;
    transform: rotate(-12deg);
  }
  .offer-badge .ellipse {
    position: absolute; left: 0; top: 22px; width: 285px; height: 92px;
    background: var(--offer-red); border-radius: 50%;
  }
  .offer-badge .lead {
    position: absolute; left: 18px; top: 4px;
    font-size: 13px; color: var(--offer-red); font-style: italic;
  }
  .offer-badge .free {
    position: absolute; left: 22px; top: 14px;
    font-size: 70px; font-weight: 700; letter-spacing: -2px;
    color: #fff; -webkit-text-stroke: 1px var(--offer-red);
  }
  .offer-badge .first {
    position: absolute; left: 26px; top: 84px;
    font-size: 20px; color: #fff;
  }

  .contact-band {
    position: absolute; left: 0; top: 583px; width: 505px; height: 132px;
    background: var(--band-grey);
  }
  .headline {
    position: absolute; left: 45px; top: 24px;
    font-size: 22px; letter-spacing: 0.5px;
  }
  .phone { position: absolute; left: 64px; top: 62px; font-size: 12px; }
  .phone strong { font-size: 22px; margin-left: 6px; letter-spacing: 0.5px; }
  .email { position: absolute; left: 44px; top: 94px; font-size: 14px; }

  .rating-card {
    position: absolute; left: 330px; top: 520px;
    width: 190px; height: 230px;
    background: var(--card-white);
    border-radius: 10px;
    box-shadow: 0 2px 8px rgba(0,0,0,0.25);
    transform: rotate(-15deg);
    padding: 26px 0 0 26px;
  }
  .rating-card li {
    list-style: none; display: flex; align-items: center; gap: 10px;
    font-size: 14px; color: #444; height: 31px;
  }
  .check { width: 20px; height: 20px; border: 2px solid #333; border-radius: 3px; position: relative; }
  .check svg { position: absolute; left: -2px; top: -10px; }
</style>
</head>
<body>
  <article class="flyer">
    <div class="hero-photo" role="img" aria-label="Photo of a modern vacuum cleaner in front of a light concrete wall beside a cream armchair"></div>

    <div class="brand">
      <span class="brand-mark"></span>
      <span class="brand-name">Brookfield Cleaners</span>
    </div>
    <p class="tagline">Premier Domestic Cleaners</p>

    <ul class="benefits">
      <li>Personalised service</li>
      <li>Constantly thorough</li>
      <li>Hassel free</li>
      <li>Insured</li>
      <li>Regular weekly cleans</li>
      <li>No contracts</li>
    </ul>

    <div class="offer-badge">
      <div class="ellipse"></div>
      <span class="lead">Allow us to demonstrate our standards...</span>
      <span class="free">FREE</span>
      <span class="first">First Clean</span>
    </div>

    <section class="contact-band">
      <h1 class="headline">RELIABLE CLEANERS!</h1>
      <p class="phone">Phone<strong>075 00 12 34 56</strong></p>
      <p class="email">email: brookfieldcleaners@example.co.uk</p>
    </section>

    <ul class="rating-card">
      <li><span class="check"><svg width="24" height="28" viewBox="0 0 24 28"><path d="M3 16 L10 24 L22 2" fill="none" stroke="#d8232a" stroke-width="3"/></svg></span>Excellent</li>
      <li><span class="check"></span>Very good</li>
      <li><span class="check"></span>Good</li>
      <li><span class="check"></span>Average</li>
      <li><span class="check"></span>Poor</li>
    </ul>
  </article>
</body>
</html>
```